Bright Fern Custom Homes business card. Double sided. Modern. professional

Bright Fern Custom Homes
contemporary modern design with our logo /
Double sided with all our contact information
Use same Green colors as in our Logo. Contemporary logo that grabs your attention. Visually pleasing and balanced. Easy to read, and Vibrant. Would love an option for rounded edges. Embossed logo would be amazing.
Contact Information for Business Card
Dana Welk Owner / General Contractor Bright Fern Custom Homes p: 704.552.1830 m: 912.648.2071 e: brightferncustomhomes@mailbox.example w: www.brightferncustomhomes.example 218 Pryor Meadow Lane Larkmoor, KV 29041

```html
<!DOCTYPE html>
<html lang="en">
<head>
<meta charset="utf-8">
<title>Bright Fern Custom Homes – Business Cards</title>
<link rel="stylesheet" href="https://fonts.googleapis.com/css2?family=Marcellus&family=Lato:wght@400&family=Arimo:wght@700&display=swap">
<style>
  :root {
    --backdrop: #d8dfc7;
    --leaf: #738a38;
    --leaf-dark: #566b25;
    --ink-green: #6b8530;
    --paper: #ffffff;
    --night: #000000;
  }
  html, body { margin: 0; padding: 0; overflow: hidden; background: var(--backdrop); }
  .board { display: block; width: 1200px; height: 1193px; }
  .card-base { fill: var(--leaf); }
  .card-panel { fill: var(--panel); }
  .edge-dark { fill: none; stroke: var(--leaf-dark); stroke-width: 5; }
  .edge-light { fill: none; stroke: var(--hairline); stroke-width: 2; }
  .wordmark { font-family: "Marcellus", serif; fill: var(--ink-green); }
  .wordmark-front { letter-spacing: 4px; }
  .wordmark-back { letter-spacing: 1.5px; }
  .wordmark-sub { font-family: "Marcellus", serif; fill: var(--ink-green); letter-spacing: 9px; }
  .brand-dot { fill: var(--ink-green); }
  .contact { font-family: "Lato", sans-serif; font-size: 15px; fill: var(--ink-green); }
  .person-name { font-family: "Arimo", sans-serif; font-weight: 700; font-size: 36px; fill: var(--ink-green); }
  .person-role { font-family: "Lato", sans-serif; font-size: 14px; fill: var(--ink-green); }
  .icon { fill: var(--ink-green); }
  .icon-line { fill: none; stroke: var(--ink-green); stroke-width: 2.5; }
  .theme-light { --panel: var(--paper); --hairline: #ffffff; }
  .theme-dark { --panel: var(--night); --hairline: #000000; }
  .lifted { filter: drop-shadow(6px 10px 8px rgba(0,0,0,0.35)); }
</style>
</head>
<body>
<svg class="board" viewBox="0 0 1448 1440" xmlns="http://www.w3.org/2000/svg">
  <defs>
    <g id="card-front">
      <rect class="card-base" x="0" y="0" width="620" height="365" rx="32"/>
      <path class="card-panel" d="M217 9 H592 Q615 9 615 32 V337 H112 L30 185 L117 34 H202 Z"/>
      <path class="edge-dark" d="M200 34 H117 L30 185"/>
      <path class="edge-light" d="M22 205 L105 350 H595"/>
      <circle class="brand-dot" cx="127" cy="180" r="46"/>
      <text class="wordmark wordmark-front" x="398" y="200" font-size="44" text-anchor="middle">BRIGHT FERN</text>
      <text class="wordmark-sub" x="400" y="215" font-size="11" text-anchor="middle">CUSTOM HOMES</text>
    </g>
    <g id="card-back">
      <rect class="card-base" x="0" y="0" width="620" height="365" rx="32"/>
      <path class="card-panel" d="M27 27 H512 L597 181 L507 331 H422 L407 357 H27 Q7 357 7 337 V47 Q7 27 27 27 Z"/>
      <path class="edge-light" d="M27 16 H522 L602 160" style="stroke: var(--leaf-dark)"/>
      <text class="wordmark wordmark-back" x="250" y="76" font-size="44" text-anchor="middle">BRIGHT FERN</text>
      <text class="wordmark-sub" x="254" y="94" font-size="11" text-anchor="middle">CUSTOM HOMES</text>

      <path class="icon" d="M34 100 a14 14 0 0 1 28 0 c0 11 -14 24 -14 38 c0 -14 -14 -27 -14 -38 z"/>
      <circle cx="48" cy="100" r="5" fill="var(--panel)"/>
      <text class="contact" x="80" y="122">218 Pryor Meadow Lane Larkmoor,</text>
      <text class="contact" x="80" y="142">KV 29041</text>

      <path class="icon" d="M33 166 l8 -4 l6 10 l-5 4 c2 6 7 11 13 14 l4 -5 l10 6 l-4 8 c-16 0 -32 -17 -32 -33 z"/>
      <path class="icon-line" d="M52 165 a10 10 0 0 1 10 10 M52 158 a17 17 0 0 1 17 17"/>
      <text class="contact" x="80" y="185">p: 704.552.1830</text>

      <rect class="icon-line" x="38" y="212" width="20" height="42" rx="3"/>
      <text class="contact" x="80" y="235">m: 912.648.2071</text>

      <rect class="icon" x="29" y="273" width="40" height="26"/>
      <path d="M29 273 L49 289 L69 273 M29 299 L44 286 M69 299 L54 286" fill="none" stroke="var(--panel)" stroke-width="2"/>
      <text class="contact" x="80" y="290">e: brightferncustomhomes@mailbox.example</text>

      <circle class="icon-line" cx="49" cy="330" r="16"/>
      <ellipse class="icon-line" cx="49" cy="330" rx="7" ry="16"/>
      <path class="icon-line" d="M33 330 H65 M36 321 H62 M36 339 H62"/>
      <text class="contact" x="80" y="337">w: www.brightferncustomhomes.example</text>

      <text class="person-name" x="570" y="191" text-anchor="end">Dana Welk</text>
      <text class="person-role" x="557" y="211" text-anchor="end">Owner / General Contractor</text>
    </g>
  </defs>

  <g class="theme-light lifted">
    <use href="#card-front" transform="translate(333 55) scale(1.266)"/>
  </g>
  <g class="theme-light"><use href="#card-front" transform="translate(78 581)"/></g>
  <g class="theme-dark"><use href="#card-front" transform="translate(755 581)"/></g>
  <g class="theme-light"><use href="#card-back" transform="translate(78 981)"/></g>
  <g class="theme-dark"><use href="#card-back" transform="translate(755 981)"/></g>
</svg>
</body>
</html>
```